Over 100 ladies will be traveling to Ocean City, MD for a Women's Retreat Conference. This flyer is for advertisement. This flyer is to circulate for registrations as well as to post on social media. Theme is Holy Spirit fire. I have attached a photo. All the information in the attachment should be included on the flyer. Information should be clearly readable end eye catching.

Target Market(s)

Church ladies

Industry/Entity Type

Religious

Font styles to use
Sans Serif

Colors

Designer to choose colors to be used in the design.

Requirements
Must have
• Title: Tidewell Womens Retreat 2019 "FIRE"
• All components in attachments

```html
<!DOCTYPE html>
<html lang="en">
<head>
<meta charset="utf-8">
<title>Tidewell Womens Retreat 2019 — FIRE Conference</title>
<link rel="stylesheet" href="https://fonts.googleapis.com/css2?family=Archivo+Black&family=Arimo:wght@400;700&family=Montserrat:wght@600;700&family=Oswald:wght@600;700&display=swap">
<style>
  :root {
    --ink: #050403;
    --white: #ffffff;
    --pink: #e8277a;
    --hot-pink: #e6337f;
    --gold: #e9b949;
    --gold-light: #ffe27a;
  }
  * { margin: 0; padding: 0; box-sizing: border-box; }
  html, body { width: 1200px; height: 900px; overflow: hidden; background: var(--ink); }
  .flyer {
    position: relative; width: 1200px; height: 900px; overflow: hidden;
    background: var(--ink);
    font-family: "Montserrat", sans-serif; color: var(--white);
  }
  .flame-field {
    position: absolute; left: 0; top: 300px; width: 1200px; height: 420px;
    background:
      radial-gradient(ellipse 420px 260px at 330px 330px, rgba(242,106,18,.85), rgba(194,38,13,.55) 55%, transparent 80%),
      radial-gradient(ellipse 380px 220px at 1050px 360px, rgba(242,106,18,.6), rgba(194,38,13,.4) 60%, transparent 85%),
      linear-gradient(180deg, transparent 0%, rgba(120,20,5,.5) 40%, rgba(194,38,13,.8) 100%);
  }
  .brand {
    position: absolute; left: 66px; top: 88px;
    font-family: "Montserrat", sans-serif; font-weight: 700; font-size: 54px;
    color: var(--pink); letter-spacing: 1px;
  }
  .event-line {
    position: absolute; left: 134px; top: 184px;
    font-family: "Montserrat", sans-serif; font-weight: 700; font-size: 43px;
    letter-spacing: 2px; color: var(--white);
  }
  .event-line .year { font-weight: 600; }
  .fire-title { position: absolute; left: 130px; top: 240px; width: 540px; height: 200px; }
  .conference-rule {
    position: absolute; left: 120px; top: 452px; width: 560px; height: 2px;
    background: linear-gradient(90deg, transparent, var(--gold-light), transparent);
  }
  .conference-rule.lower { top: 507px; }
  .conference {
    position: absolute; left: 120px; top: 462px; width: 560px; text-align: center;
    font-family: "Arimo", sans-serif; font-size: 33px; letter-spacing: 22px; color: var(--white);
    padding-left: 22px;
  }
  .speakers-badge { position: absolute; left: 216px; top: 548px; width: 361px; height: 44px; }
  .speakers-badge span {
    position: absolute; inset: 0; display: flex; align-items: center; justify-content: center;
    font-family: "Oswald", sans-serif; font-weight: 700; font-size: 30px; color: #111; letter-spacing: .5px;
  }
  .info-band {
    position: absolute; left: 0; top: 712px; width: 1200px; height: 125px;
    background: linear-gradient(90deg, var(--hot-pink) 0%, #f14a8c 45%, #f7a060 75%, var(--hot-pink) 100%);
  }
  .speaker-photo {
    position: absolute; top: 611px; width: 152px; height: 154px;
    border: 4px solid #d9c9a6;
    background: linear-gradient(180deg, #f4f4f4 0%, #e6e6e6 55%, #2a2a2a 100%);
  }
  .speaker-photo.one { left: 193px; }
  .speaker-photo.two { left: 445px; }
  .speaker-name {
    position: absolute; top: 774px; width: 260px; text-align: center;
    font-family: "Arimo", sans-serif; color: #111;
  }
  .speaker-name.one { left: 138px; }
  .speaker-name.two { left: 396px; }
  .speaker-name strong { display: block; font-weight: 700; font-size: 20px; line-height: 25px; }
  .speaker-name span { display: block; font-size: 19px; line-height: 24px; }
  .host-photo, .host-frame { position: absolute; left: 705px; top: 115px; width: 448px; height: 618px; }
  .host-credit {
    position: absolute; left: 737px; top: 752px; width: 400px; text-align: center;
    font-family: "Arimo", sans-serif; color: #111;
  }
  .host-credit .role { display: block; font-size: 30px; line-height: 34px; }
  .host-credit .name { display: block; font-weight: 700; font-size: 31px; line-height: 36px; }
  .contact {
    position: absolute; left: 0; top: 845px; width: 1200px;
    font-family: "Arimo", sans-serif; font-size: 19px; letter-spacing: 2px; color: var(--white);
    display: flex; justify-content: center; align-items: center; gap: 6px;
  }
  .contact strong { font-weight: 700; }
  .contact svg { width: 18px; height: 18px; }
</style>
</head>
<body>
<main class="flyer">
  <div class="flame-field" role="img" aria-label="Background of rising flames and smoke"></div>

  <div class="brand">Tidewell</div>
  <div class="event-line">WOMEN’S TREAT <span class="year">2019</span></div>

  <svg class="fire-title" viewBox="0 0 540 200" aria-label="FIRE">
    <defs>
      <linearGradient id="fireFill" x1="0" y1="0" x2="0" y2="1">
        <stop offset="0" stop-color="#ffe27a"/>
        <stop offset=".45" stop-color="#f58a1f"/>
        <stop offset="1" stop-color="#c2260d"/>
      </linearGradient>
    </defs>
    <text x="270" y="186" text-anchor="middle" textLength="530" lengthAdjust="spacingAndGlyphs"
          font-family="Archivo Black, sans-serif" font-size="200" fill="url(#fireFill)">FIRE</text>
  </svg>

  <div class="conference-rule"></div>
  <div class="conference">CONFERENCE</div>
  <div class="conference-rule lower"></div>

  <svg class="speakers-badge" viewBox="0 0 361 44" preserveAspectRatio="none" aria-hidden="true">
    <defs>
      <linearGradient id="badgeGold" x1="0" y1="0" x2="0" y2="1">
        <stop offset="0" stop-color="#ffe98a"/>
        <stop offset=".5" stop-color="#e9b949"/>
        <stop offset="1" stop-color="#b9852c"/>
      </linearGradient>
    </defs>
    <polygon points="10,0 351,0 361,22 351,44 10,44 0,22" fill="url(#badgeGold)" stroke="#8a5f1c" stroke-width="1.5"/>
  </svg>
  <div class="speakers-badge"><span>RETREAT SPEAKERS:</span></div>

  <div class="info-band"></div>

  <div class="speaker-photo one" role="img" aria-label="Portrait of Pastor Renata Hale"></div>
  <div class="speaker-photo two" role="img" aria-label="Portrait of Pastor Celeste Moore"></div>

  <div class="speaker-name one"><strong>Pastor Renata Hale</strong><span>GLCM - Bowie, Md.</span></div>
  <div class="speaker-name two"><strong>Pastor Celeste Moore</strong><span>Orlando, Florida</span></div>

  <svg class="host-photo" viewBox="0 0 448 618" role="img" aria-label="Portrait of retreat host Apostle Dorinda Wells">
    <defs>
      <linearGradient id="hostFill" x1="0" y1="0" x2="0" y2="1">
        <stop offset="0" stop-color="#4a1022"/>
        <stop offset="1" stop-color="#d8306f"/>
      </linearGradient>
    </defs>
    <path d="M80 38 H368 V66 H410 V534 L224 578 L38 534 V66 H80 Z" fill="url(#hostFill)"/>
  </svg>

  <svg class="host-frame" viewBox="0 0 448 618" aria-hidden="true">
    <defs>
      <linearGradient id="frameGold" x1="0" y1="0" x2="1" y2="1">
        <stop offset="0" stop-color="#ffe27a"/>
        <stop offset=".5" stop-color="#c9953a"/>
        <stop offset="1" stop-color="#ffe27a"/>
      </linearGradient>
    </defs>
    <path d="M46 2 H402 V30 H446 V560 L224 616 L2 560 V30 H46 Z" fill="none" stroke="url(#frameGold)" stroke-width="4"/>
    <path d="M58 16 H390 V44 H432 V550 L224 600 L16 550 V44 H58 Z" fill="none" stroke="url(#frameGold)" stroke-width="2"/>
    <path d="M72 30 H376 V58 H418 V540 L224 586 L30 540 V58 H72 Z" fill="none" stroke="#e9b949" stroke-width="3" stroke-dasharray="2 7" stroke-linecap="round"/>
  </svg>

  <div class="host-credit">
    <span class="role">Retreat Host:</span>
    <span class="name">Apostle Dorinda Wells</span>
  </div>

  <div class="contact">
    <span>For more information please contact</span>
    <svg viewBox="0 0 20 20" aria-hidden="true"><g fill="none" stroke="#fff" stroke-width="1.5"><circle cx="10" cy="10" r="8.5"/><ellipse cx="10" cy="10" rx="3.8" ry="8.5"/><line x1="1.5" y1="10" x2="18.5" y2="10"/><line x1="3" y1="5.5" x2="17" y2="5.5"/><line x1="3" y1="14.5" x2="17" y2="14.5"/></g></svg>
    <strong>www.dorindawellsministries.com</strong>
    <svg viewBox="0 0 20 20" aria-hidden="true"><rect x="1" y="1" width="18" height="18" rx="4" fill="#fff"/><path d="M6.5 4.5 L8.5 4.5 L9.3 7.5 L8 8.6 Q9 11 11.4 12 L12.5 10.7 L15.5 11.5 L15.5 13.5 Q15 15.5 12.8 15.3 Q5 14 4.7 7.2 Q4.6 4.8 6.5 4.5 Z" fill="#050403"/></svg>
    <strong>240-555-0148</strong>
  </div>
</main>
</body>
</html>
```